Customs House descriptive business cards

We require a two-sided business card that has a simple yet elegant design. We want to be able to promote our services as a customs house. This card should include our logo, contact info and services offered with the logo being on one side and the contact info and services on the flip side

Target Market(s)

Importers / exporters to and from the Bahamas

Industry/Entity Type

Logistics

Contact Information for Business Card

The front side of the card could have the logo and the flip side should have the other relevant info

Font styles to use
Serif

Colors

Designer to choose colors to be used in the design.

Requirements
Must have
• (Harbourline Agents Ltd) Logo, address and contact info also services:
• import customs clearance, Delivery & HAndling services,Florida pickups, Export packing & Crating Services, export customs clearance, Consulting

```html
<!DOCTYPE html>
<html lang="en">
<head>
<meta charset="utf-8">
<title>Harbourline Agents Ltd – Business Card</title>
<link rel="stylesheet" href="https://fonts.googleapis.com/css2?family=Cinzel:wght@400&family=Open+Sans:wght@400;600&display=swap">
<style>
  :root {
    --backdrop: #2a2a2c;
    --card-dark: #111113;
    --card-light: #ffffff;
    --brand-blue: #2389d0;
    --ink-grey: #3f3f42;
    --band-grey: #bdbdbf;
    --name-grey: #4a4a4c;
  }
  * { margin: 0; padding: 0; box-sizing: border-box; }
  html, body { width: 1200px; height: 900px; overflow: hidden; }
  body {
    background: var(--backdrop);
    font-family: "Open Sans", Arial, sans-serif;
    position: relative;
  }
  .card {
    position: absolute;
    left: 250px;
    width: 700px;
    height: 400px;
    overflow: hidden;
    box-shadow: 0 10px 30px rgba(0,0,0,0.5);
  }
  .card--front { top: 40px; background: var(--card-dark); }
  .card--back { top: 470px; background: var(--card-light); }

  .brand {
    position: absolute;
    display: flex;
    flex-direction: column;
    align-items: center;
    gap: 14px;
  }
  .brand__mark {
    border-radius: 50%;
    background: var(--brand-blue);
  }
  .brand__name {
    font-family: "Open Sans", Arial, sans-serif;
    font-weight: 600;
    white-space: nowrap;
  }
  .card--front .brand { left: 0; right: 0; top: 110px; }
  .card--front .brand__mark { width: 86px; height: 86px; }
  .card--front .brand__name { font-size: 30px; color: var(--band-grey); }

  .card--back .brand { left: 40px; width: 290px; top: 62px; gap: 10px; }
  .card--back .brand__mark { width: 64px; height: 64px; }
  .card--back .brand__name { font-size: 21px; color: var(--ink-grey); }

  .contact {
    position: absolute;
    left: 380px; top: 74px;
    color: var(--ink-grey);
  }
  .contact__name {
    font-family: "Cinzel", Georgia, serif;
    font-weight: 400;
    font-size: 28px;
    letter-spacing: 1px;
    color: var(--name-grey);
  }
  .contact__title {
    font-size: 15px;
    color: var(--brand-blue);
    margin-top: -2px;
  }
  .contact__list { list-style: none; margin-top: 18px; }
  .contact__item {
    display: flex; align-items: center; gap: 12px;
    font-size: 17px; margin-bottom: 6px;
  }
  .contact__item svg { width: 18px; height: 18px; flex: none; fill: var(--brand-blue); }

  .services {
    position: absolute;
    left: 40px; top: 246px; width: 640px;
    font-size: 16.5px;
    color: var(--ink-grey);
    line-height: 1.6;
  }
  .bands { position: absolute; left: 0; bottom: 0; width: 700px; height: 70px; }
</style>
</head>
<body>

<section class="card card--front" aria-label="Card front">
  <div class="brand">
    <span class="brand__mark" aria-hidden="true"></span>
    <h1 class="brand__name">Harbourline Agents Ltd</h1>
  </div>
</section>

<section class="card card--back" aria-label="Card back">
  <div class="brand">
    <span class="brand__mark" aria-hidden="true"></span>
    <div class="brand__name">Harbourline Agents Ltd</div>
  </div>

  <div class="contact">
    <div class="contact__name">Your Name</div>
    <div class="contact__title">JOB TITLE</div>
    <ul class="contact__list">
      <li class="contact__item">
        <svg viewBox="0 0 24 24"><path d="M3 9c0-3 4-5 9-5s9 2 9 5v2h-5V9H8v2H3zM6 12h12l2 8H4z"/></svg>
        000 000 0000
      </li>
      <li class="contact__item">
        <svg viewBox="0 0 24 24"><path d="M2 5h20v14H2zM3.5 6.5 12 13l8.5-6.5" fill="none" stroke="#2389d0" stroke-width="2"/></svg>
        youremail@xyz.com
      </li>
      <li class="contact__item">
        <svg viewBox="0 0 24 24"><path d="M12 2a7 7 0 0 0-7 7c0 5 7 13 7 13s7-8 7-13a7 7 0 0 0-7-7zm0 10a3 3 0 1 1 0-6 3 3 0 0 1 0 6z"/></svg>
        youraddresshere
      </li>
    </ul>
  </div>

  <p class="services">
    Import Customs Clearance &nbsp;|&nbsp; Delivery &amp; Handling Services &nbsp;|&nbsp; Florida pickups<br>
    Export packing &amp; Crating Services &nbsp;|&nbsp; Export Customs Clearance &nbsp;|&nbsp; Consulting
  </p>

  <svg class="bands" viewBox="0 0 700 70" aria-hidden="true">
    <polygon points="0,4 450,4 430,38 0,38" fill="var(--brand-blue)"/>
    <polygon points="462,20 700,20 700,70 432,70" fill="var(--band-grey)"/>
  </svg>
</section>

</body>
</html>
```